Individual Needs Design for Marketing Package

****IMPORTANT: Note that I have arranged an agreement with a specific designer to complete the design for the portfolio. Please do not submit any designs***

Goal
I recently resigned from my job in Canada, and I am moving down to Silicon Valley to pursue a career in the technology startup scene - initially doing technical sales. So my goal is to get a sales position with a startup tech company.

In order to land a sales position, I will be going to a startup conference in Silicon Valley which brings together over 2,000 startup technology companies. My goal is to meet the owners of some of these companies and demonstrate that I can be a valuable asset to their company. My challenge is that I have no existing relationships in Silicon Valley and limited experience in sales. So I have put together a portfolio of some of my most significant accomplishments over the past 6 years (see attached file). My hope is that this portfolio will convey that even though I have limited experience, I am passionate, driven, and loyal with a proven track record of achievement. After talking with them for 30 minutes and developing a rapport, I plan on giving this accomplishment portfolio (in addition to my resume) to CEOs of companies for which I could potentially work.

Message to Communicate
After someone reads my portfolio, I want them to view me as passionate, driven, and loyal with a proven track record of achievement. The design can communicate this message in a subtle way. The portfolio should also speak to my professionalism. It should certainly have some personality, but it should err on the side of professionalism.

Competitors
My competitors will be other people at the conference also looking to get sales positions with these startup companies. My main points of differentiation are that I am passionate, driven, and loyal with a proven track record of results. I would like this to be made a feature of the design.

Design Templates
I do not have any specific fonts or colours that I need you to use. The colours scheme and fonts selected should reinforce my key message.

Other Information
I do not own any specialized design software - only the basic microsoft word and powerpoint. However, I will need to be able to add new accomplishments to the portfolio and edit existing ones. Please let me know how this will be possible. I am not sure if it is possible to convert the final file into a file format that I can edit.

Notice that I have arranged the pages into sections. Feel free to rearrange the content within the sections, but please do not change the order of the sections

The size for the marketing package will be regular 8.5 x 11".
Updates

Target Market(s)

The people that will be reading my portfolio are owners of small technology companies in Silicon Valley. They are typically 28-35 years old, and highly logical thinkers. This means that the content is what is ultimately going to sell myself, but the design is what will make them want to read it. Therefore, the content should really stand out over the design.

Industry/Entity Type

Marketing

Requirements
Must have
• ****IMPORTANT: Note that I have arranged an agreement with a specific designer to complete the design for the portfolio. Please do not submit any designs***

I really view this portfolio as my personal marketing package, and that is where I need your expertise. I need you to take the content that I have in my portfolio and turn it into a personal marketing package. I need you to:

1. Design the cover page
2. Design the template for the content pages
3. Format the pictures and text to best fit the design of the pages**

** I would like the final design submission to include the pictures and text included in the attached file all fully formatted. However, when submitting the first iterations, please do not feel obligated to format the entire portfolio because I know that it can be time consuming. Just formatting the title page and the first content page should be enough to give me an idea of what the final portfolio will look like. Once we narrow it down to the final few designs, then we can start formatting the complete portfolio.

```html
<!DOCTYPE html>
<html lang="en">
<head>
<meta charset="utf-8">
<title>Daniel Morrow — Portfolio of Accomplishments</title>
<link rel="stylesheet" href="https://fonts.googleapis.com/css2?family=Questrial&family=Source+Sans+3:wght@400&display=swap">
<style>
  :root {
    --cover-ground: #ebebec;
    --label-white: #ffffff;
    --accent-green: #6ab651;
    --name-grey: #6d6e71;
    --subtitle-blue: #1ba4e0;
    --url-purple: #7a4f9e;
  }
  html, body {
    margin: 0;
    padding: 0;
    width: 946px;
    height: 1200px;
    overflow: hidden;
  }
  .cover {
    position: relative;
    width: 946px;
    height: 1200px;
    overflow: hidden;
    background: var(--cover-ground);
    font-family: "Source Sans 3", "Myriad Pro", Arial, sans-serif;
  }
  .cover__pattern {
    position: absolute;
    inset: 0;
    background: linear-gradient(180deg, #eeeeef 0%, #e8e8ea 100%);
  }
  .cover__band {
    position: absolute;
    left: 420px;
    width: 107px;
    background: var(--accent-green);
  }
  .cover__band--top { top: 0; height: 720px; }
  .cover__band--bottom { top: 1045px; height: 155px; }
  .title-label {
    position: absolute;
    left: 186px;
    top: 734px;
    width: 595px;
    height: 297px;
    background: var(--label-white);
    text-align: center;
  }
  .title-label__owner {
    position: absolute;
    left: 0;
    right: 0;
    top: 26px;
    margin: 0;
    font-size: 36px;
    font-weight: 400;
    color: var(--name-grey);
    line-height: 1;
  }
  .title-label__heading {
    position: absolute;
    left: 0;
    right: 0;
    top: 84px;
    margin: 0;
    font-family: "Questrial", "Century Gothic", sans-serif;
    font-size: 84px;
    font-weight: 400;
    color: var(--accent-green);
    line-height: 1;
    letter-spacing: -1px;
  }
  .title-label__subheading {
    position: absolute;
    left: 0;
    right: 0;
    top: 180px;
    margin: 0;
    font-size: 28px;
    color: var(--subtitle-blue);
    line-height: 1;
  }
  .title-label__rule {
    position: absolute;
    left: 168px;
    top: 225px;
    width: 261px;
    height: 2px;
    background: var(--subtitle-blue);
  }
  .title-label__url {
    position: absolute;
    left: 0;
    right: 0;
    top: 251px;
    margin: 0;
    font-size: 16px;
    letter-spacing: 0.6px;
    color: var(--url-purple);
    line-height: 1;
  }
</style>
</head>
<body>
  <main class="cover">
    <div class="cover__pattern" role="img" aria-label="Subtle light grey hexagonal lace pattern covering the page"></div>
    <div class="cover__band cover__band--top"></div>
    <div class="cover__band cover__band--bottom"></div>
    <section class="title-label">
      <p class="title-label__owner">Daniel Morrow’s</p>
      <h1 class="title-label__heading">PORTFOLIO</h1>
      <p class="title-label__subheading">of Accomplishments</p>
      <div class="title-label__rule"></div>
      <p class="title-label__url">www.danielmorrow.com</p>
    </section>
  </main>
</body>
</html>
```